Electrical company 7Oaks needs a new logo design.

Need business cards for electrical company.
Modern/luxury/ Smart.
Thinking Black with White text.
Attached the logo below.

We would like two versions made - each one having different contact information on (one for each company directors). Both however will have same company address -

Fenwick Court 31-35 Harrow Lane
Northmere Isle
Harbrook Date
SS4 7QP

Contact details 1 -
Gareth Pemberton
Director
gary@7oaks.example.co.uk
07700958312

Contact details 2 -
Kieron Haskett
Director
07700946271
kieron@7oaks.example.co.uk

Logo Text

7 Oaks Electrical Solutions

```html
<!DOCTYPE html>
<html lang="en">
<head>
<meta charset="utf-8">
<title>Director Business Cards</title>
<link rel="stylesheet" href="https://fonts.googleapis.com/css2?family=Montserrat:wght@300;400;600&display=swap">
<style>
  :root {
    --sheet: #b3b3b3;
    --paper: #ffffff;
    --ink: #111111;
    --night: #000000;
    --gold: #c4a25a;
    --light: #ffffff;
  }
  * { margin: 0; padding: 0; box-sizing: border-box; }
  html, body { width: 1200px; height: 725px; overflow: hidden; }
  body {
    position: relative;
    background: var(--sheet);
    font-family: "Montserrat", Arial, sans-serif;
  }
  .card {
    position: absolute;
    width: 543px;
    height: 326px;
    overflow: hidden;
  }
  .card--front { background: var(--paper); color: var(--ink); top: 27px; }
  .card--back  { background: var(--night); color: var(--light); top: 378px; }
  .card--left  { left: 30px; }
  .card--right { left: 626px; }

  .brand {
    position: absolute;
    left: 42px;
    top: 38px;
    display: flex;
    align-items: center;
    gap: 14px;
  }
  .brand__mark {
    width: 14px;
    height: 14px;
    background: var(--gold);
  }
  .brand__name {
    font-size: 46px;
    font-weight: 300;
    line-height: 52px;
    letter-spacing: 0.18em;
    color: var(--ink);
    text-transform: uppercase;
  }

  .address {
    position: absolute;
    left: 43px;
    top: 210px;
    font-size: 14.5px;
    font-weight: 400;
    line-height: 18.3px;
    font-style: normal;
  }

  .contact {
    position: absolute;
    left: 146px;
    top: 114px;
  }
  .contact__name {
    font-size: 17px;
    font-weight: 600;
    letter-spacing: 0.01em;
    line-height: 20px;
  }
  .contact__role {
    font-size: 15px;
    font-weight: 400;
    line-height: 20px;
    margin-bottom: 9px;
  }
  .contact__line {
    display: flex;
    align-items: center;
    gap: 9px;
    font-size: 15px;
    font-weight: 400;
    height: 29px;
  }
  .contact__icon {
    width: 16px;
    height: 16px;
    flex: none;
  }
</style>
</head>
<body>

  <section class="card card--front card--left">
    <div class="brand">
      <span class="brand__mark"></span>
      <span class="brand__name">7 Oaks</span>
    </div>
    <address class="address">
      Fenwick Court 31-35 Harrow Lane<br>
      Northmere Isle<br>
      Harbrook Date<br>
      SS4 7QP
    </address>
  </section>

  <section class="card card--front card--right">
    <div class="brand">
      <span class="brand__mark"></span>
      <span class="brand__name">7 Oaks</span>
    </div>
    <address class="address">
      Fenwick Court 31-35 Harrow Lane<br>
      Northmere Isle<br>
      Harbrook Date<br>
      SS4 7QP
    </address>
  </section>

  <section class="card card--back card--left">
    <div class="contact">
      <p class="contact__name">Gareth Pemberton</p>
      <p class="contact__role">Director</p>
      <p class="contact__line">
        <svg class="contact__icon" viewBox="0 0 16 16" aria-hidden="true">
          <rect width="16" height="16" rx="2" fill="var(--gold)"/>
          <rect x="3" y="4.5" width="10" height="7" fill="none" stroke="#000" stroke-width="1.1"/>
          <path d="M3 4.5 L8 8.5 L13 4.5" fill="none" stroke="#000" stroke-width="1.1"/>
        </svg>
        gary@7oaks.example.co.uk
      </p>
      <p class="contact__line">
        <svg class="contact__icon" viewBox="0 0 16 16" aria-hidden="true">
          <rect width="16" height="16" rx="2" fill="var(--gold)"/>
          <path d="M4.5 3.5 L6.5 3.5 L7.3 6 L6 7 Q7 9.2 9 10 L10 8.7 L12.5 9.5 L12.5 11.5 Q12 12.6 10.5 12.5 Q5 11.5 3.5 5.5 Q3.5 4 4.5 3.5 Z" fill="#000"/>
        </svg>
        07700958312
      </p>
    </div>
  </section>

  <section class="card card--back card--right">
    <div class="contact">
      <p class="contact__name">Kieron Haskett</p>
      <p class="contact__role">Director</p>
      <p class="contact__line">
        <svg class="contact__icon" viewBox="0 0 16 16" aria-hidden="true">
          <rect width="16" height="16" rx="2" fill="var(--gold)"/>
          <rect x="3" y="4.5" width="10" height="7" fill="none" stroke="#000" stroke-width="1.1"/>
          <path d="M3 4.5 L8 8.5 L13 4.5" fill="none" stroke="#000" stroke-width="1.1"/>
        </svg>
        kieron@7oaks.example.co.uk
      </p>
      <p class="contact__line">
        <svg class="contact__icon" viewBox="0 0 16 16" aria-hidden="true">
          <rect width="16" height="16" rx="2" fill="var(--gold)"/>
          <path d="M4.5 3.5 L6.5 3.5 L7.3 6 L6 7 Q7 9.2 9 10 L10 8.7 L12.5 9.5 L12.5 11.5 Q12 12.6 10.5 12.5 Q5 11.5 3.5 5.5 Q3.5 4 4.5 3.5 Z" fill="#000"/>
        </svg>
        07700946271
      </p>
    </div>
  </section>

</body>
</html>
```